Communications Contractor Business Card Design

I would like a new business card for a new Communications company in Australia. Subcontracting and specialising in cabling, data, phone, antennas, pay tv ,modems, audio visual fibre optics etc. I am open to colour and design concepts but would like a modern clean look that stands out.

Industry/Entity Type

Tv

Contact Information for Business Card

kestrel communications pty ltd, Doug Pemberton, PO BOX 657 Marlow Flats QLD 4873 kestrel4me@maildrop-example.com Australia. ph 0437196084. Director/Technician. services- Cabling,data,phone,antennas,audio visual,home theatre, fibre optics.

```html
<!DOCTYPE html>
<html lang="en">
<head>
<meta charset="utf-8">
<title>Kestrel Communications – Business Card</title>
<link rel="stylesheet" href="https://fonts.googleapis.com/css2?family=Mulish:wght@400;600;700;900&display=swap">
<style>
  :root {
    --bg: #2a2a2c;
    --card: #f7f7f7;
    --red: #d4161c;
    --teal: #2fb8c2;
    --ink: #333333;
    --muted: #555555;
    --white: #ffffff;
  }
  * { box-sizing: border-box; margin: 0; padding: 0; }
  html, body { width: 1200px; height: 900px; overflow: hidden; }
  body {
    background: var(--bg);
    font-family: "Mulish", sans-serif;
    position: relative;
  }
  .card {
    position: absolute;
    left: 250px;
    width: 700px;
    height: 400px;
    background: var(--card);
    border-radius: 4px;
    overflow: hidden;
    box-shadow: 0 10px 30px rgba(0,0,0,.5);
  }
  .card--back { top: 40px; }
  .card--front { top: 470px; }
  .card__bands { position: absolute; left: 0; bottom: 0; width: 700px; height: 400px; }

  .brand {
    position: absolute;
    color: var(--red);
    font-weight: 900;
    text-transform: uppercase;
    line-height: 0.95;
    letter-spacing: 0.5px;
  }
  .brand__line { display: block; }
  .card--back .brand { left: 150px; top: 70px; font-size: 38px; }
  .card--front .brand { left: 60px; top: 60px; font-size: 38px; }
  .brand__suffix { font-size: 20px; letter-spacing: 2px; }

  .services-tag {
    position: absolute;
    left: 40px; bottom: 60px;
    background: var(--teal);
    color: var(--white);
    font-weight: 600;
    font-size: 20px;
    padding: 6px 16px;
    border-radius: 8px;
  }
  .services {
    position: absolute;
    top: 190px;
    left: 330px;
    display: flex;
    gap: 50px;
    list-style: none;
    color: var(--muted);
    font-size: 18px;
    line-height: 1.35;
  }
  .services ul { list-style: none; }
  .services .col-a { padding-top: 60px; }

  .person { position: absolute; right: 60px; top: 175px; text-align: left; }
  .person__name { font-weight: 700; font-size: 24px; color: var(--ink); }
  .person__role {
    display: inline-block;
    margin-top: 2px;
    background: var(--teal);
    color: var(--white);
    font-size: 13px;
    padding: 2px 10px;
    border-radius: 4px;
  }

  .contact-icons {
    position: absolute;
    left: 0; top: 250px;
    width: 42px; height: 120px;
    background: var(--teal);
    border-radius: 0 8px 8px 0;
    display: flex; flex-direction: column; justify-content: space-around; align-items: center;
  }
  .contact {
    position: absolute;
    left: 70px; top: 262px;
    color: var(--ink);
    font-size: 19px;
    line-height: 1.35;
  }
  .contact__phone { margin-bottom: 14px; }
</style>
</head>
<body>

  <section class="card card--back" aria-label="Card back">
    <div class="brand">
      <span class="brand__line">Kestrel</span>
      <span class="brand__line">Communications</span>
      <span class="brand__line brand__suffix">Pty Ltd</span>
    </div>
    <div class="services">
      <ul class="col-a">
        <li>-Data,</li>
        <li>-Cabling,</li>
        <li>-Phone,</li>
      </ul>
      <ul class="col-b">
        <li>-Antennas,</li>
        <li>-Audio Visual,</li>
        <li>-Home Theatre,</li>
        <li>-Fibre Optics.</li>
      </ul>
    </div>
    <div class="services-tag">Our Services:-</div>
    <svg class="card__bands" viewBox="0 0 700 400" aria-hidden="true">
      <rect x="0" y="370" width="500" height="18" fill="var(--teal)"/>
      <path d="M480 400 V372 Q480 346 508 346 H700 V400 Z" fill="var(--red)"/>
    </svg>
  </section>

  <section class="card card--front" aria-label="Card front">
    <div class="brand">
      <span class="brand__line">Kestrel</span>
      <span class="brand__line">Communications</span>
      <span class="brand__line brand__suffix">Pty Ltd</span>
    </div>
    <div class="person">
      <div class="person__name">Doug Pemberton</div>
      <div class="person__role">Director/Technician</div>
    </div>
    <div class="contact-icons">
      <svg width="24" height="22" viewBox="0 0 24 22" aria-label="Phone" role="img">
        <path d="M2 7 Q12 0 22 7 L19 10 L16 8 V6 Q12 4 8 6 V8 L5 10 Z" fill="var(--white)"/>
        <rect x="4" y="11" width="16" height="10" rx="2" fill="var(--white)"/>
        <circle cx="12" cy="16" r="2.5" fill="var(--teal)"/>
      </svg>
      <svg width="20" height="26" viewBox="0 0 20 26" aria-label="Location" role="img">
        <path d="M10 1 C4.5 1 1 5 1 10 C1 16 10 25 10 25 C10 25 19 16 19 10 C19 5 15.5 1 10 1 Z" fill="var(--white)"/>
        <circle cx="10" cy="10" r="3.5" fill="var(--teal)"/>
      </svg>
    </div>
    <div class="contact">
      <p class="contact__phone">0437196084</p>
      <p>PO BOX 657 Marlow Flats,</p>
      <p>QLD 4873 Australia</p>
    </div>
    <svg class="card__bands" viewBox="0 0 700 400" aria-hidden="true">
      <rect x="0" y="370" width="500" height="18" fill="var(--teal)"/>
      <path d="M480 400 V372 Q480 346 508 346 H700 V400 Z" fill="var(--red)"/>
    </svg>
  </section>

</body>
</html>
```